New Boutique Pilates and Barre studio needs a flyer to promote classes.

Our studio is called 'The Willow Loft'. We are a boutique studio in Sydney that offers pilates mat and Barre classes with a maximum of 8 participants.

We need a flyer to promote our new studio that is opening mid-January 2015. Our goal is to motivate clients to cherish and nurture their bodies by participating in either our Pilates mat classes and/or our barre classes.

The flyer needs to communicate high-end, boutique classes that welcome those aged from 17-70 who would like achieve a stronger, leaner and dancer-like physique.

We would like our logo and a picture on the front with our contact details . The front should also say "First class is free!" (somewhere down the bottom).

A description of our classes as well as a map of our location should be on the back. Please see attached word document for copy.
I have attached our logo and contact details as well as pictures that may be used.

Please keep it uncluttered and elegant.
Updates

I have added a few pilates photos and a few requirements for the front of the flyer. Thanks

Industry/Entity Type

Boutique

Requirements
Must have

• MUST INCLUDE ON THE FRONT:
Please make sure my logo is very clear.

* Barre Classes
* Pilates Mat Classes
Private Studio in Castle Hill, Sydney
'First Class is free!'
Contact details: (Phone, website, email and address)

```html
<!DOCTYPE html>
<html lang="en">
<head>
<meta charset="utf-8">
<title>The Willow Loft – Barre &amp; Pilates Mat Classes</title>
<link rel="stylesheet" href="https://fonts.googleapis.com/css2?family=Raleway:wght@300;400;600;700&display=swap">
<style>
  :root {
    --ink: #555a60;
    --ink-strong: #3a3d42;
    --navy: #233a8c;
    --navy-light: #3a5cb8;
    --headline: #2f4f9e;
    --orange: #f18a22;
    --white: #ffffff;
    --sky: #6fb4dc;
  }
  * { box-sizing: border-box; margin: 0; padding: 0; }
  html, body { width: 899px; height: 1200px; overflow: hidden; background: var(--white); }
  body { font-family: "Raleway", Arial, sans-serif; color: var(--ink); }
  .flyer { position: relative; width: 899px; height: 1200px; overflow: hidden; }

  .hero { position: absolute; top: 0; left: 0; width: 899px; height: 180px; }

  .copy { position: absolute; left: 72px; width: 756px; font-size: 18px; line-height: 24.5px; text-align: justify; font-weight: 400; }
  .intro { top: 229px; }
  .barre-copy { top: 351px; }
  .pilates-lead { top: 569px; font-weight: 700; color: var(--ink-strong); }
  .pilates-copy { top: 652px; }
  .benefits { top: 730px; }
  .benefits ul { list-style: none; }
  .benefits li { padding-left: 0; }
  .benefits li::before { content: ""; display: inline-block; width: 7px; height: 7px; border-radius: 50%; background: var(--navy); margin-right: 4px; vertical-align: middle; position: relative; top: -2px; }

  .section-tab {
    position: absolute; left: 0; height: 26px;
    background: linear-gradient(90deg, var(--navy) 0%, var(--navy) 60%, var(--navy-light) 100%);
    border-radius: 0 13px 13px 0;
    color: var(--white); font-weight: 700; font-size: 17px; line-height: 26px;
    padding-left: 72px;
  }
  .tab-barre { top: 315px; width: 232px; }
  .tab-pilates { top: 532px; width: 284px; }

  .headline { position: absolute; top: 922px; left: 0; width: 899px; text-align: center; color: var(--headline); font-weight: 700; font-size: 24px; line-height: 29px; }

  .brand { position: absolute; top: 1040px; left: 0; width: 899px; text-align: center; }
  .brand-name { font-size: 44px; font-weight: 400; color: var(--navy); letter-spacing: 1px; }

  .offer { position: absolute; left: 0; top: 1143px; width: 899px; height: 57px; background: var(--orange); color: var(--white); text-align: center; font-size: 40px; font-weight: 300; line-height: 57px; letter-spacing: 1px; }
</style>
</head>
<body>
<main class="flyer">
  <svg class="hero" viewBox="0 0 899 180" xmlns="http://www.w3.org/2000/svg">
    <defs>
      <linearGradient id="photo-a" x1="0" y1="0" x2="0" y2="1"><stop offset="0" stop-color="#c9ccd2"/><stop offset="1" stop-color="#5b6470"/></linearGradient>
      <linearGradient id="photo-b" x1="0" y1="0" x2="0" y2="1"><stop offset="0" stop-color="#e8ebee"/><stop offset="1" stop-color="#c9a9a0"/></linearGradient>
      <linearGradient id="photo-c" x1="0" y1="0" x2="0" y2="1"><stop offset="0" stop-color="#e4e7ea"/><stop offset="1" stop-color="#4aa3d6"/></linearGradient>
      <linearGradient id="photo-d" x1="0" y1="0" x2="1" y2="1"><stop offset="0" stop-color="#9bb06a"/><stop offset="1" stop-color="#3f5a3a"/></linearGradient>
      <linearGradient id="wave-band" x1="0" y1="0" x2="1" y2="0"><stop offset="0" stop-color="#233a8c"/><stop offset="0.6" stop-color="#3a6fc4"/><stop offset="1" stop-color="#7cc0e6"/></linearGradient>
    </defs>
    <rect x="0" y="0" width="217" height="180" fill="url(#photo-a)" role="img" aria-label="Photo of a Pilates class stretching forward over small balls on mats"/>
    <rect x="219" y="0" width="225" height="180" fill="url(#photo-b)" role="img" aria-label="Photo of a smiling woman side-stretching with an arm overhead"/>
    <rect x="446" y="0" width="226" height="180" fill="url(#photo-c)" role="img" aria-label="Photo of a mixed-age group stretching forward on blue mats"/>
    <rect x="674" y="0" width="225" height="180" fill="url(#photo-d)" role="img" aria-label="Photo of a woman in a dress dancing outdoors among trees"/>
    <path d="M0 150 C 250 190, 560 175, 899 118 L899 140 C 560 192, 250 200, 0 168 Z" fill="url(#wave-band)"/>
    <path d="M0 160 C 250 198, 560 190, 899 132 L899 180 L0 180 Z" fill="#ffffff"/>
  </svg>

  <p class="copy intro">The Willow Loft is a boutique studio In Castle Hill, Sydney.  We offer Pilates mat and barre classes for adults of any age, who are seeking a stronger, leaner dancer –like physique.</p>

  <h2 class="section-tab tab-barre">Barre classes:</h2>
  <div class="copy barre-copy">
    <p>Our Barre classes are a 50 minute fusion of Pilates, dance and total body strengthening through the use of the ballet barre, light hand weights, pilates balls and body weight.</p>
    <p>We move to the latest upbeat pop style music, making it fun and easy to forget that you are working out!   Best of all, you do not need to be a dancer or have any kind of dance experience to join in. If you love moving to music then this class is just right for you.</p>
  </div>

  <h2 class="section-tab tab-pilates">Pilates Mat classes:</h2>
  <p class="copy pilates-lead">Pilates is a body-conditioning program designed to teach efficient movement patterns and provide general well-being using controlled exercises and deliberate breathing patterns.</p>
  <p class="copy pilates-copy">Our Pilates mat classes consist of a 50 minute routine based on Joseph Hallam matwork exercises that include props such as therabands, balls, foam rollers, light weights and a barre to challenge balance and lower body strength and stability.</p>
  <div class="copy benefits">
    <p>Pilates offers benefits such as improvement in:</p>
    <ul>
      <li>Core strength,</li>
      <li>Body tone,</li>
      <li>Flexibility,</li>
      <li>Posture,</li>
      <li>Efficient movement, and</li>
      <li>Mind/Body connection.</li>
    </ul>
  </div>

  <p class="headline">All off our classes have a maximum of 8 participants,<br>so reserve your space today!</p>

  <div class="brand"><span class="brand-name">The Willow Loft</span></div>

  <p class="offer">FIRST CLASS IS FREE!</p>
</main>
</body>
</html>
```